Business Card Design Project - velmora

We are building an agency for innovative solutions in marketing, education and events to pharmaceutical companies, physicians, medical societies, patient advocacy groups. We want to become a reference in this market in Brazil as the most boutique agency here. We deal with every detail with a lot of love and caring for what we do like craftsmen.
Our card must show innovation and inspiration. Yet should be clean. Something like Swiss design, quint design, etc.
Reason: I think the initial time was too short. I believe with more time you can exceed expectations. I'm liking a lot this experience
Target Market(s)
Pharmaceutical companies, doctors and patients
Industry/Entity Type
Pharmaceutical
Font styles to use
Other font styles liked:
- Helvetia family
Colors
Designer to choose colors to be used in the design.
Requirements
Must have
- Modern, clean,
Nice to have
- Innovative idea to show
Should not have
- Not too appear too much Comercial. Must be modern but sober.

```html
<!DOCTYPE html>
<html lang="en">
<head>
<meta charset="utf-8">
<title>velmora — business card</title>
<link rel="stylesheet" href="https://fonts.googleapis.com/css2?family=Jost:wght@400;500&family=Rokkitt:wght@400;500&display=swap">
<style>
  :root {
    --backdrop: #d9d9d9;
    --paper: #ffffff;
    --leaf: #86c84f;
    --leaf-light: #97d266;
    --ink: #111111;
    --night: #000000;
    --brand-blue: #3c80c4;
    --card-w: 520px;
    --card-h: 297px;
  }
  * { box-sizing: border-box; margin: 0; padding: 0; }
  html, body {
    width: 1200px;
    height: 864px;
    overflow: hidden;
  }
  body {
    background: var(--backdrop);
    display: flex;
    align-items: center;
    justify-content: center;
    gap: 60px;
  }
  .card {
    width: var(--card-w);
    height: var(--card-h);
    position: relative;
    overflow: hidden;
    box-shadow: 0 6px 18px rgba(0,0,0,0.18);
  }
  .wordmark {
    font-family: "Jost", sans-serif;
    font-weight: 500;
    color: var(--brand-blue);
    letter-spacing: 0.5px;
    line-height: 1;
  }

  /* front */
  .card--front { background: var(--paper); }
  .card--front .band {
    position: absolute;
    left: 0; right: 0; bottom: 0;
    height: 68%;
    background: radial-gradient(ellipse at 45% 40%, var(--leaf-light), var(--leaf) 75%);
  }
  .card--front .wordmark {
    position: absolute;
    top: 34px;
    left: 0; right: 0;
    text-align: center;
    font-size: 46px;
  }
  .contact {
    position: absolute;
    top: 114px;
    left: 0; right: 0;
    text-align: center;
    color: var(--ink);
  }
  .contact .person {
    font-family: "Rokkitt", serif;
    font-size: 27px;
    font-weight: 500;
    line-height: 1;
  }
  .contact .role {
    font-family: "Rokkitt", serif;
    font-size: 17px;
    line-height: 1.1;
    margin-bottom: 14px;
  }
  .contact .line {
    font-family: "Jost", sans-serif;
    font-size: 17px;
    line-height: 1.35;
  }

  /* back */
  .card--back { background: var(--night); }
  .card--back .wordmark {
    position: absolute;
    top: 58px;
    right: 34px;
    font-size: 56px;
  }
</style>
</head>
<body>
  <section class="card card--front" aria-label="Card front">
    <div class="band"></div>
    <div class="wordmark">velmora</div>
    <div class="contact">
      <p class="person">Daniel Roe</p>
      <p class="role">Project Manager</p>
      <p class="line">+1 (555) 0142 376</p>
      <p class="line">48 Lindell St., Harborview, NY 10044</p>
      <p class="line">P.O. Box: 408615</p>
      <p class="line">hello@velmora.com</p>
    </div>
  </section>

  <section class="card card--back" aria-label="Card back">
    <div class="wordmark">velmora</div>
  </section>
</body>
</html>
```